CBD Company needs bag design made

Our company is creating CBD gummies which we need a design based off the dimensions of the AI file provided. I have included some base designs for basic ideas. The flavors are as follows "Blue Raspberry" .. "Tropical Fruit" .. "Fizzlot" (which is a sour strawberry) and "Watermelon" I included the mock ups of the bags as well as some zoomed in pictures of two the labels as well to give a little better of a reference. Our company name is Corvanta which we would like instead of Dapplets (Corvanta logo attached). The final design should display what's in each bag (4 separate bag designs) with images depicting that in addition the to Corvana Logo(ai attached). I attached the nutritional facts as well which should match the color schemes of each flavor (where the blue color is in the image attached to match the flavor example: Blue Raspberry = blue) this will be located on the back of the bag.

```html
<!DOCTYPE html>
<html lang="en">
<head>
<meta charset="utf-8">
<title>Corvanta CBD Gummies – Bag Fronts</title>
<link href="https://fonts.googleapis.com/css2?family=Rubik:wght@300;500;700&display=swap" rel="stylesheet">
<style>
  :root {
    --page: #ffffff;
    --bag: #f1f1f1;
    --seal-line: #d6d6d6;
    --ink: #2a2a2a;
    --white: #ffffff;
  }
  html, body { margin: 0; padding: 0; overflow: hidden; }
  body {
    width: 1200px; height: 1200px; background: var(--page);
    position: relative; font-family: "Rubik", sans-serif;
  }
  .blue-raspberry { --deep: #1846c8; --mid: #2f6cf0; --light: #6f9cf5; --band: #aebddf; --band-ink: #1b3fa0; --badge: #1f80f2; --accent: #1b3fa0; }
  .tropical-fruit { --deep: #c45a12; --mid: #e07c24; --light: #f0a55a; --band: #efccb0; --band-ink: #c0580f; --badge: #c85a0e; --accent: #d2641a; }
  .fizzlot        { --deep: #a11f78; --mid: #c9359a; --light: #e070bd; --band: #f0b9da; --band-ink: #a8247e; --badge: #ff2d88; --accent: #b32a86; }
  .watermelon     { --deep: #c81e24; --mid: #e8393b; --light: #f47a74; --band: #f1baba; --band-ink: #d42225; --badge: #ff2a1a; --accent: #d82a2d; }

  .bag {
    position: absolute; width: 368px; height: 590px; background: var(--bag);
  }
  .bag.top { top: 0; }
  .bag.bottom { top: 610px; }
  .bag.left { left: 212px; }
  .bag.right { left: 621px; }
  .seal { position: absolute; left: 0; right: 0; height: 0; border-top: 1px solid var(--seal-line); }
  .seal.upper { top: 118px; }
  .seal.dashed { top: 138px; border-top: 1px dashed var(--seal-line); }
  .seal.lower { top: 155px; }

  .label {
    position: absolute; left: 24px; top: 158px; width: 320px; height: 404px; overflow: hidden;
  }
  .label-photo {
    position: absolute; left: 0; top: 0; width: 320px; height: 336px;
    background: radial-gradient(circle at 30% 25%, var(--light), var(--mid) 45%, var(--deep) 100%);
  }
  .brand {
    position: absolute; left: 0; width: 320px; top: 14px; text-align: center; color: var(--white);
  }
  .brand-dot {
    width: 44px; height: 44px; border-radius: 50%; background: var(--white); margin: 0 auto 8px;
  }
  .brand-name { font-weight: 300; font-size: 30px; line-height: 28px; letter-spacing: 0.5px; }
  .brand-sub { font-weight: 300; font-size: 30px; line-height: 28px; }

  .flavor-card {
    position: absolute; left: 49px; top: 150px; width: 236px; height: 172px;
    background: var(--white); border-radius: 44px 44px 52px 52px;
  }
  .flavor-name {
    margin: 22px 0 0; text-align: center; font-weight: 700; font-size: 18px; line-height: 21px;
    color: var(--ink); letter-spacing: 0.2px;
  }
  .gummy-shot {
    position: absolute; left: 42px; top: 78px; width: 90px; height: 74px; border-radius: 10px;
    background: linear-gradient(135deg, var(--light), var(--deep));
  }
  .fruit-shot {
    position: absolute; left: 140px; top: 84px; width: 72px; height: 62px; border-radius: 30px;
    background: radial-gradient(circle, var(--mid), var(--deep));
  }
  .tropical-fruit .fruit-shot { background: radial-gradient(circle, #f2c63a, #4f9a2c); }
  .watermelon .fruit-shot { background: radial-gradient(circle, #f05a5a, #2f7d2a); }
  .fizzlot .fruit-shot { background: radial-gradient(circle, #e22a2a, #3a1a3a); }

  .clarity-seal {
    position: absolute; left: 7px; top: 205px; width: 66px; height: 66px; border-radius: 50%;
    background: var(--white); border: 2px solid var(--accent); box-sizing: border-box;
    display: flex; align-items: center; justify-content: center; text-align: center;
    color: var(--accent); font-weight: 700; font-size: 9.5px; line-height: 10.5px;
  }

  .info-band {
    position: absolute; left: 0; top: 336px; width: 320px; height: 68px; background: var(--band);
    color: var(--ink);
  }
  .serving { position: absolute; left: 13px; top: 14px; font-size: 8px; line-height: 12px; font-weight: 500; letter-spacing: 0.3px; }
  .net-weight { position: absolute; left: 13px; top: 46px; font-size: 8.5px; font-weight: 500; color: var(--band-ink); }
  .cbd-tag {
    position: absolute; left: 243px; top: 18px; width: 62px; height: 34px; box-sizing: border-box;
    border: 2px solid var(--band-ink); border-radius: 7px; color: var(--band-ink);
    font-weight: 700; font-size: 21px; line-height: 30px; text-align: center;
  }

  .dose-badge {
    position: absolute; left: 266px; top: 131px; width: 78px; height: 78px; border-radius: 50%;
    background: var(--badge); color: var(--white); font-weight: 700; font-size: 14px; line-height: 17px;
    display: flex; flex-direction: column; align-items: center; justify-content: center;
    transform: rotate(-18deg);
  }
</style>
</head>
<body>

<section class="bag top left blue-raspberry">
  <div class="seal upper"></div><div class="seal dashed"></div><div class="seal lower"></div>
  <div class="label">
    <div class="label-photo" role="img" aria-label="Close-up of sugared blue raspberry gummies"></div>
    <div class="brand"><div class="brand-dot"></div><div class="brand-name">Corvanta</div><div class="brand-sub">CBD</div></div>
    <div class="flavor-card">
      <h2 class="flavor-name">BLUE RASPBERRY<br>GUMMIES</h2>
      <div class="gummy-shot" role="img" aria-label="Stack of blue gummy cubes"></div>
      <div class="fruit-shot" role="img" aria-label="Blue raspberries"></div>
    </div>
    <div class="clarity-seal">HIGH<br>CLARITY<br>CBD<br>EXRACT</div>
    <div class="info-band">
      <div class="serving">1 PIECE PER SERVING<br>10 SERVINGS PER PACKAGE</div>
      <div class="net-weight">Net Weight 2.5 oz, 70g</div>
      <div class="cbd-tag">CBD</div>
    </div>
  </div>
  <div class="dose-badge"><span>250mg</span><span>CBD</span></div>
</section>

<section class="bag top right tropical-fruit">
  <div class="seal upper"></div><div class="seal dashed"></div><div class="seal lower"></div>
  <div class="label">
    <div class="label-photo" role="img" aria-label="Close-up of sugared orange tropical gummies"></div>
    <div class="brand"><div class="brand-dot"></div><div class="brand-name">Corvanta</div><div class="brand-sub">CBD</div></div>
    <div class="flavor-card">
      <h2 class="flavor-name">TROPICAL FRUIT<br>GUMMIES</h2>
      <div class="gummy-shot" role="img" aria-label="Stack of orange gummy cubes"></div>
      <div class="fruit-shot" role="img" aria-label="Pineapple and tropical fruits"></div>
    </div>
    <div class="clarity-seal">HIGH<br>CLARITY<br>CBD<br>EXRACT</div>
    <div class="info-band">
      <div class="serving">1 PIECE PER SERVING<br>10 SERVINGS PER PACKAGE</div>
      <div class="net-weight">Net Weight 2.5 oz, 70g</div>
      <div class="cbd-tag">CBD</div>
    </div>
  </div>
  <div class="dose-badge"><span>250mg</span><span>CBD</span></div>
</section>

<section class="bag bottom left fizzlot">
  <div class="seal upper"></div><div class="seal dashed"></div><div class="seal lower"></div>
  <div class="label">
    <div class="label-photo" role="img" aria-label="Close-up of sugared magenta berry gummies"></div>
    <div class="brand"><div class="brand-dot"></div><div class="brand-name">Corvanta</div><div class="brand-sub">CBD</div></div>
    <div class="flavor-card">
      <h2 class="flavor-name">FIZZLOT<br>GUMMIES</h2>
      <div class="gummy-shot" role="img" aria-label="Stack of magenta gummy cubes"></div>
      <div class="fruit-shot" role="img" aria-label="Strawberries and blackberries"></div>
    </div>
    <div class="clarity-seal">HIGH<br>CLARITY<br>CBD<br>EXRACT</div>
    <div class="info-band">
      <div class="serving">1 PIECE PER SERVING<br>10 SERVINGS PER PACKAGE</div>
      <div class="net-weight">Net Weight 2.5 oz, 70g</div>
      <div class="cbd-tag">CBD</div>
    </div>
  </div>
  <div class="dose-badge"><span>250mg</span><span>CBD</span></div>
</section>

<section class="bag bottom right watermelon">
  <div class="seal upper"></div><div class="seal dashed"></div><div class="seal lower"></div>
  <div class="label">
    <div class="label-photo" role="img" aria-label="Close-up of sugared red watermelon gummies"></div>
    <div class="brand"><div class="brand-dot"></div><div class="brand-name">Corvanta</div><div class="brand-sub">CBD</div></div>
    <div class="flavor-card">
      <h2 class="flavor-name">WATERMELON<br>GUMMIES</h2>
      <div class="gummy-shot" role="img" aria-label="Stack of red gummy cubes"></div>
      <div class="fruit-shot" role="img" aria-label="Watermelon and slices"></div>
    </div>
    <div class="clarity-seal">HIGH<br>CLARITY<br>CBD<br>EXRACT</div>
    <div class="info-band">
      <div class="serving">1 PIECE PER SERVING<br>10 SERVINGS PER PACKAGE</div>
      <div class="net-weight">Net Weight 2.5 oz, 70g</div>
      <div class="cbd-tag">CBD</div>
    </div>
  </div>
  <div class="dose-badge"><span>250mg</span><span>CBD</span></div>
</section>

</body>
</html>
```